Poster Design Project

We are launching a new company Q Vyn, we sell advertising on digital signage and we are launching our company selling ads at our 2 locations, Marlow Bend Sports and Rec Club and the Tresgold Reef Sports and Rec Club. We want to advertise that we have 5 10 and 15 ad slots available and ads start from as little as $27.00 per week. We need to let people know we offer 10% discount to LWBTO members. it needs to have the following contact details to get more information, Gideon 0479352104 and gideon@qvyn.com.au. As a new launch we are offering for the first 10 customers one of 2 discounts, get 4 weeks free all you have to pay is the content creation fee ($99 for 5 second ad) or 4 weeks free and free content creation if you sign up to a 18 week contract.

Update: need the add to start wit something like this but you can be creative:

Need to get you message or brand out, Have you heard of digital sinage?
We have ads avaliable starting from $27 per week at one of our locations.

Or something like that, as i am introducing my company they dont know what i do you untill they read this poster.

Target Market(s)

Targeting small to medium buisness

Industry/Entity Type

Advertising

Requirements
Must have
• Logo

```html
<!DOCTYPE html>
<html lang="en">
<head>
<meta charset="utf-8">
<title>Q Vyn – Digital Signage Ads</title>
<link rel="stylesheet" href="https://fonts.googleapis.com/css2?family=Anton&family=Montserrat:wght@600;800&display=swap">
<style>
  :root {
    --bg-core: #27303d;
    --bg-edge: #151b24;
    --type-light: #c9d1d2;
    --type-depth: #6f7879;
    --type-shade: rgba(0, 0, 0, 0.55);
    --type-soft: #aab4b6;
    --burst: #b9c3c5;
    --burst-ink: #1d2430;
    --rule: rgba(201, 209, 210, 0.25);
    --brand-white: #ffffff;
    --brand-blue: #1e8fd6;
  }

  * { margin: 0; padding: 0; box-sizing: border-box; }

  html, body {
    width: 847px;
    height: 1200px;
    overflow: hidden;
    background: var(--bg-edge);
  }

  .poster {
    position: relative;
    width: 847px;
    height: 1200px;
    overflow: hidden;
    background: radial-gradient(ellipse 75% 60% at 50% 45%, var(--bg-core) 0%, var(--bg-edge) 100%);
    font-family: "Anton", "Impact", sans-serif;
    color: var(--type-light);
  }

  .headline-line,
  .offer-lead,
  .offer-tail {
    position: absolute;
    display: block;
    font-weight: 400;
    text-transform: uppercase;
    white-space: nowrap;
    line-height: 1;
    color: var(--type-light);
    text-shadow:
      1px 1px 0 var(--type-depth),
      2px 2px 0 var(--type-depth),
      3px 3px 0 var(--type-depth),
      4px 4px 0 var(--type-depth),
      5px 5px 0 var(--type-depth),
      8px 10px 12px var(--type-shade);
  }

  .headline-line--intro { left: 88px; top: 64px;  font-size: 45px; }
  .headline-line--ask   { left: 86px; top: 120px; font-size: 82px; }
  .headline-line--topic { left: 80px; top: 196px; font-size: 98px; }

  .offer-lead { left: 68px; top: 344px; font-size: 46px; }

  .price-burst {
    position: absolute;
    left: 214px;
    top: 404px;
    width: 420px;
    height: 420px;
    filter: drop-shadow(10px 14px 16px rgba(0, 0, 0, 0.55));
  }
  .price-burst .burst-shape { fill: var(--burst); }
  .price-burst .burst-price {
    font-family: "Anton", "Impact", sans-serif;
    font-size: 230px;
    fill: var(--burst-ink);
  }

  .offer-tail { left: 30px; top: 846px; font-size: 49px; }

  .details {
    position: absolute;
    left: 40px;
    right: 40px;
    top: 914px;
    font-family: "Montserrat", "Arial", sans-serif;
    text-align: center;
    color: var(--type-soft);
  }

  .locations {
    font-size: 16px;
    font-weight: 800;
    color: var(--type-light);
    text-transform: uppercase;
    letter-spacing: 0.3px;
  }

  .perks {
    margin-top: 10px;
    padding: 10px 0;
    border-top: 1px solid var(--rule);
    border-bottom: 1px solid var(--rule);
    list-style: none;
    font-size: 14px;
    font-weight: 600;
    line-height: 1.5;
  }
  .perks strong { font-weight: 800; color: var(--type-light); }

  .brand {
    position: absolute;
    left: 0;
    right: 0;
    top: 1070px;
    display: flex;
    align-items: center;
    justify-content: center;
    gap: 20px;
  }
  .brand-mark {
    width: 54px;
    height: 54px;
    background: var(--brand-blue);
  }
  .brand-name {
    font-family: "Anton", "Impact", sans-serif;
    font-size: 58px;
    line-height: 1;
    color: var(--brand-white);
  }

  .contact {
    position: absolute;
    left: 0;
    right: 0;
    top: 1150px;
    font-family: "Montserrat", "Arial", sans-serif;
    font-size: 17px;
    font-weight: 800;
    text-align: center;
    color: var(--type-light);
  }
  .contact-sep { color: var(--brand-blue); padding: 0 10px; }
</style>
</head>
<body>
  <main class="poster">
    <h1 class="headline">
      <span class="headline-line headline-line--intro">Need to get your message or brand out,</span>
      <span class="headline-line headline-line--ask">Have you heard</span>
      <span class="headline-line headline-line--topic">of digital signage?</span>
    </h1>

    <p class="offer-lead">Ads available starting from</p>

    <svg class="price-burst" viewBox="-230 -230 460 460" role="img" aria-label="$27">
      <polygon class="burst-shape" points="215,0 175.9,27.8 204.5,66.4 158.6,80.8 173.9,126.4 125.9,125.9 126.4,173.9 80.8,158.6 66.4,204.5 27.8,175.9 0,215 -27.8,175.9 -66.4,204.5 -80.8,158.6 -126.4,173.9 -125.9,125.9 -173.9,126.4 -158.6,80.8 -204.5,66.4 -175.9,27.8 -215,0 -175.9,-27.8 -204.5,-66.4 -158.6,-80.8 -173.9,-126.4 -125.9,-125.9 -126.4,-173.9 -80.8,-158.6 -66.4,-204.5 -27.8,-175.9 0,-215 27.8,-175.9 66.4,-204.5 80.8,-158.6 126.4,-173.9 125.9,-125.9 173.9,-126.4 158.6,-80.8 204.5,-66.4 175.9,-27.8"/>
      <text class="burst-price" x="0" y="80" text-anchor="middle" transform="rotate(-4)">$27</text>
    </svg>

    <p class="offer-tail">Per week at one of our locations</p>

    <section class="details">
      <p class="locations">Marlow Bend Sports and Rec Club &nbsp;·&nbsp; Tresgold Reef Sports and Rec Club</p>
      <ul class="perks">
        <li><strong>5, 10 &amp; 15 ad slots available</strong> &nbsp;·&nbsp; <strong>10% off</strong> for LWBTO members</li>
        <li><strong>First 10 customers:</strong> 4 weeks free – pay only the $99 content fee (5 second ad)</li>
        <li>or 4 weeks free <strong>plus free content creation</strong> on an 18 week contract</li>
      </ul>
    </section>

    <div class="brand">
      <span class="brand-mark"></span>
      <span class="brand-name">Q Vyn</span>
    </div>

    <p class="contact">Gideon<span class="contact-sep">|</span>0479352104<span class="contact-sep">|</span>gideon@qvyn.com.au</p>
  </main>
</body>
</html>
```